I need a business card design for a Boutique Pilates studio.

I would like to see designs similar to the one that I have uploaded.
thinking between two slogans:
'No ordinary place'
'Not so ordinary'

Contact Information for Business Card

Keva Pilates

```html
<!DOCTYPE html>
<html lang="en">
<head>
<meta charset="utf-8">
<title>Keva Pilates – Business Card</title>
<link rel="stylesheet" href="https://fonts.googleapis.com/css2?family=Oswald:wght@300;500&family=Great+Vibes&family=Open+Sans:wght@400&display=swap">
<style>
  :root {
    --backdrop: #2a2b2c;
    --card: #464646;
    --ink-dark: #141414;
    --ink-soft: #1c1c1c;
    --accent: #f2cc00;
  }
  * { box-sizing: border-box; margin: 0; padding: 0; }
  html, body {
    width: 1200px;
    height: 939px;
    overflow: hidden;
    background: var(--backdrop);
  }
  .canvas {
    position: relative;
    width: 1200px;
    height: 939px;
  }
  .card {
    position: absolute;
    left: 300px;
    width: 600px;
    height: 343px;
    background: var(--card);
    box-shadow: 0 10px 30px rgba(0,0,0,0.45);
  }
  .card--front { top: 80px; }
  .card--back  { top: 500px; }

  /* Front */
  .brand {
    position: absolute;
    left: 0; right: 0;
    top: 112px;
    text-align: center;
    font-family: 'Oswald', sans-serif;
    font-weight: 300;
    font-size: 54px;
    letter-spacing: 6px;
    color: var(--ink-soft);
    white-space: nowrap;
  }
  .tagline {
    position: absolute;
    left: 0; right: 0;
    top: 200px;
    text-align: center;
    font-family: 'Oswald', sans-serif;
    font-weight: 500;
    font-size: 14px;
    letter-spacing: 7px;
    color: var(--ink-dark);
    white-space: nowrap;
  }

  /* Back */
  .identity {
    position: absolute;
    left: 30px;
    top: 132px;
    width: 274px;
    text-align: right;
    color: var(--accent);
    white-space: nowrap;
  }
  .identity__name {
    font-family: 'Great Vibes', cursive;
    font-size: 44px;
    line-height: 1;
  }
  .identity__role {
    font-family: 'Open Sans', sans-serif;
    font-size: 14px;
    letter-spacing: 1.5px;
    margin-top: 2px;
  }
  .divider {
    position: absolute;
    left: 318px;
    top: 128px;
    width: 1.5px;
    height: 76px;
    background: var(--accent);
  }
  .contact {
    position: absolute;
    left: 334px;
    top: 130px;
    list-style: none;
    font-family: 'Open Sans', sans-serif;
    font-size: 14px;
    letter-spacing: 0.6px;
    color: var(--accent);
    white-space: nowrap;
  }
  .contact__item {
    display: flex;
    align-items: center;
    gap: 6px;
    height: 24px;
  }
  .contact__icon { width: 11px; height: 11px; flex: none; }
</style>
</head>
<body>
<main class="canvas">
  <section class="card card--front" aria-label="Card front">
    <div class="brand">Keva Pilates</div>
    <div class="tagline">NO ORDINARY PLACE...</div>
  </section>

  <section class="card card--back" aria-label="Card back">
    <div class="identity">
      <div class="identity__name">Liam Hartley</div>
      <div class="identity__role">Owner</div>
    </div>
    <div class="divider"></div>
    <ul class="contact">
      <li class="contact__item">
        <svg class="contact__icon" viewBox="0 0 12 12" aria-hidden="true">
          <path d="M2.5 0.8 L4.5 0.8 L5.2 3.4 L3.9 4.4 C4.6 6 6 7.4 7.6 8.1 L8.6 6.8 L11.2 7.5 L11.2 9.5 C11.2 10.4 10.4 11.2 9.5 11.2 C4.7 11 1 7.3 0.8 2.5 C0.8 1.6 1.6 0.8 2.5 0.8 Z" fill="var(--accent)"/>
        </svg>
        <span>0400 318 562</span>
      </li>
      <li class="contact__item">
        <svg class="contact__icon" viewBox="0 0 12 12" aria-hidden="true">
          <rect x="0.5" y="2" width="11" height="8" fill="var(--accent)"/>
          <path d="M0.5 2 L6 6.5 L11.5 2" fill="none" stroke="var(--card)" stroke-width="1"/>
        </svg>
        <span>info@KevaPilates.com.au</span>
      </li>
      <li class="contact__item">
        <svg class="contact__icon" viewBox="0 0 12 12" aria-hidden="true">
          <circle cx="6" cy="6" r="5.2" fill="none" stroke="var(--accent)" stroke-width="1.2"/>
          <ellipse cx="6" cy="6" rx="2.3" ry="5.2" fill="none" stroke="var(--accent)" stroke-width="1"/>
          <path d="M0.8 6 H11.2 M1.6 3.4 H10.4 M1.6 8.6 H10.4" stroke="var(--accent)" stroke-width="0.9"/>
        </svg>
        <span>KevaPilates.com.au</span>
      </li>
    </ul>
  </section>
</main>
</body>
</html>
```